Detox Drink Needs A Label for a drug testing company

About Us
The company name is “Pillwise”, we are a diagnostic test provider specialising in the distribution and manufacturing of drug testing kits. Our end user is both commercial and private clients with over 70% being the later of the two.

About the product
The product I am marketing is a urine detox drink aimed at removing drug metabolites from the urine, there are currently a number of similar products on the market; Zephropure, Vortex Calrin, Flowmarva, none of which are made in Australia.

We are looking to enter this market with an Australia made and owned product that works in much the same way
but is available locally for distribution.

We currently have another product on the market which works in much the same way but to remove drug metabolites from the saliva in order to prevent false positives on a drugntest.

The Renal Rinse will work by diuretic action, promoting urination by osmotic release,effectively diluting drug metabolites.

What we are after
What we are after is a label to suit a 500ML bottle that contains various information including company logo, nutritional Information which will need to be editable, size, flavour etc. Product name – Renal Rinse / Purge – Zero Flavour – Watermelon , Grape

We would like to keep a professional but modern look that makes our product come across as more pharmaceutical rather than the energy drink look that our competitors are running
with.

Industry/Entity Type

Health Product

Colors
33a6d7
f3f1f8
fbf289
33b8a4

Requirements
Must have
• Flavour; Grape, Watermelon, Lemon Line (must be editable text)
• Brand Logo
• Colorful Graphics
• Full wrap around label
• Nutritional Information on the rear with editable text
• Renal Rinse
• Helps to cleanse the urine of drug metabolites

```html
<!DOCTYPE html>
<html lang="en">
<head>
<meta charset="UTF-8">
<title>Pillwise – Renal Rinse Label</title>
<link rel="stylesheet" href="https://fonts.googleapis.com/css2?family=Roboto+Condensed:wght@700&family=Caveat:wght@500&display=swap">
<style>
  :root {
    --ink: #2a2a2a;
    --teal: #33a896;
    --teal-mark: #4fa89c;
    --sky-deep: #0f7fd3;
    --sky-mid: #3d9fe0;
    --sky-pale: #d6ebf9;
    --paper: #ffffff;
    --sun-pale: #fff6c8;
    --sun: #fbd25a;
    --amber: #f39a1c;
    --ember: #ea7a0c;
  }
  html, body {
    margin: 0;
    padding: 0;
    overflow: hidden;
    background: var(--paper);
  }
  .label {
    position: relative;
    width: 1200px;
    height: 720px;
    overflow: hidden;
    background: var(--paper);
    font-family: "Roboto Condensed", "Arial Narrow", sans-serif;
  }
  .wave-top {
    position: absolute;
    left: 0; top: 0;
    width: 1200px; height: 280px;
    background:
      radial-gradient(ellipse 420px 150px at 1080px 40px, var(--sky-deep), transparent 80%),
      radial-gradient(ellipse 460px 110px at 170px 130px, var(--sky-mid), transparent 80%),
      radial-gradient(ellipse 520px 70px at 900px 210px, rgba(61,159,224,0.55), transparent 80%),
      linear-gradient(180deg, var(--sky-pale) 0%, rgba(214,235,249,0.7) 60%, rgba(255,255,255,0) 100%);
  }
  .wave-bottom {
    position: absolute;
    left: 0; top: 400px;
    width: 1200px; height: 320px;
    background:
      radial-gradient(ellipse 520px 200px at 100px 300px, var(--ember), transparent 80%),
      radial-gradient(ellipse 480px 150px at 1080px 250px, var(--amber), transparent 80%),
      radial-gradient(ellipse 600px 60px at 300px 80px, rgba(243,154,28,0.55), transparent 80%),
      linear-gradient(180deg, rgba(255,246,200,0) 0%, var(--sun-pale) 25%, var(--sun) 70%, var(--amber) 100%);
  }
  .brand {
    position: absolute;
    left: 454px; top: 70px;
    width: 292px; height: 111px;
    display: flex;
    align-items: center;
    justify-content: center;
    gap: 12px;
  }
  .brand-dot {
    width: 28px; height: 28px;
    border-radius: 50%;
    background: var(--teal-mark);
  }
  .brand-name {
    font-size: 40px;
    font-weight: 700;
    color: var(--ink);
  }
  .product-name {
    position: absolute;
    left: 0; top: 312px;
    width: 1200px;
    margin: 0;
    text-align: center;
    font-size: 82px;
    font-weight: 700;
    line-height: 1;
    color: var(--ink);
  }
  .flavour {
    position: absolute;
    left: 0; top: 470px;
    width: 1200px;
    margin: 0;
    text-align: center;
    font-family: "Caveat", cursive;
    font-size: 58px;
    font-weight: 500;
    line-height: 1;
    letter-spacing: 2px;
    color: var(--teal);
  }
  .tagline {
    position: absolute;
    left: 0; top: 666px;
    width: 1200px;
    margin: 0;
    text-align: center;
    font-size: 34px;
    font-weight: 700;
    line-height: 1;
    color: var(--ink);
  }
</style>
</head>
<body>
  <main class="label">
    <div class="wave-top" role="img" aria-label="Flowing blue ribbon lines sweeping across the top"></div>
    <div class="wave-bottom" role="img" aria-label="Flowing orange and yellow ribbon lines sweeping across the bottom"></div>

    <div class="brand">
      <span class="brand-dot"></span>
      <span class="brand-name">Pillwise</span>
    </div>

    <h1 class="product-name">Renal Rinse</h1>
    <p class="flavour">Grape Flavour</p>
    <p class="tagline">Helps to cleanse the urine of drug metabolites</p>
  </main>
</body>
</html>
```